Rural photograpy business card design

I need a business card for my photography business, marisol dovey photography. I would like my logo and pre designed font used on the card. Also my business specialises in photographing rural australia (e.g. shearing sheds, livestock, landscapes, farms), so a rural or country feel to the card would be great. I would like to keep the colours fresh but not too overpowering or juvenile.

Hi,

Could you please add my facebook page to the card - www.snapfolk.net/Marisol/Dovey/Photography.
Thanks,
Marisol.

Reason: I have uploaded two photos I would like either one used on the card.

Target Market(s)

Farmers, country people from their mid twenties onwards

Industry/Entity Type

Business

Contact Information for Business Card

Marisol Dovey Photography. Marisol Pendergast. 1295 Wirrabilla-Kontee Road, Kontee Qld 4871. 0471620394.

Requirements
Must have
• My pre-designed logo and font. Also please add my facebook address - www.snapfolk.net/MarisolDovey/Photography.
Please use one of the photos I have provided.
Should not have
• Peoples faces on the card.

```html
<!DOCTYPE html>
<html lang="en">
<head>
<meta charset="utf-8">
<title>Marisol Dovey Photography – Business Card</title>
<link href="https://fonts.googleapis.com/css2?family=Oswald:wght@200;300;400&display=swap" rel="stylesheet">
<style>
  :root {
    --backdrop: #b7c6d4;
    --card-yellow: #ffe000;
    --card-yellow-deep: #f7d200;
    --ink: #4a4a45;
    --white: #ffffff;
    --band: rgba(120, 92, 70, 0.72);
    --corner-gold: #f2d21a;
    --sky-light: #f6f0a6;
    --sky-warm: #d9c25a;
    --earth-mid: #8a6f4d;
    --earth-dark: #3e2f22;
  }
  * { box-sizing: border-box; margin: 0; padding: 0; }
  html, body { width: 1200px; height: 840px; overflow: hidden; }
  body {
    background: var(--backdrop);
    font-family: "Oswald", "Arial Narrow", sans-serif;
    display: flex;
    flex-direction: column;
    align-items: center;
    justify-content: center;
    gap: 28px;
  }
  .card {
    position: relative;
    width: 640px;
    height: 366px;
    overflow: hidden;
    box-shadow: 0 6px 18px rgba(40, 60, 80, 0.18);
  }
  .corner-marks { position: absolute; inset: 0; width: 100%; height: 100%; pointer-events: none; }

  /* Front */
  .card-front .photo {
    position: absolute; inset: 0;
    background:
      radial-gradient(ellipse 30% 26% at 86% 58%, rgba(255, 240, 150, 0.95), rgba(255, 230, 120, 0) 70%),
      linear-gradient(180deg, var(--sky-light) 0%, var(--sky-warm) 38%, var(--earth-mid) 62%, var(--earth-dark) 100%);
  }
  .title-band {
    position: absolute;
    left: 52px; right: 52px;
    top: 122px; height: 78px;
    background: var(--band);
    display: flex; align-items: center; justify-content: center;
  }
  .title-band svg { position: absolute; inset: 0; width: 100%; height: 100%; }
  .business-name {
    color: var(--white);
    font-weight: 300;
    font-size: 44px;
    letter-spacing: 0.5px;
    text-transform: uppercase;
    white-space: nowrap;
  }

  /* Back */
  .card-back {
    background: linear-gradient(160deg, var(--card-yellow) 0%, var(--card-yellow-deep) 100%);
    color: var(--ink);
  }
  .owner {
    position: absolute;
    left: 58px; top: 110px;
    width: 220px; height: 130px;
    display: flex; align-items: center; justify-content: center;
  }
  .owner svg { position: absolute; inset: 0; width: 100%; height: 100%; }
  .owner-name {
    font-weight: 300;
    font-size: 38px;
    line-height: 1.05;
    text-transform: uppercase;
    text-align: center;
  }
  .divider {
    position: absolute;
    left: 318px; top: 82px;
    width: 1px; height: 200px;
    background: var(--ink);
  }
  .contact-list {
    position: absolute;
    left: 350px; top: 108px;
    list-style: none;
    display: flex; flex-direction: column; gap: 26px;
  }
  .contact-item {
    display: flex; align-items: center; gap: 12px;
    font-weight: 300;
    font-size: 15px;
    line-height: 1.25;
    max-width: 270px;
  }
  .contact-item svg { flex: 0 0 26px; width: 26px; height: 26px; }
  .contact-phone { font-size: 20px; letter-spacing: 1px; }
</style>
</head>
<body>

  <section class="card card-front" aria-label="Business card front">
    <div class="photo" role="img" aria-label="Photograph of a flock of sheep in a rural yard at sunset, with gum trees and a golden hazy sky"></div>
    <div class="title-band">
      <svg viewBox="0 0 536 78" preserveAspectRatio="none" aria-hidden="true">
        <g fill="none" stroke="#ffffff" stroke-width="1.5">
          <polyline points="2,14 2,2 14,2"/>
          <polyline points="522,2 534,2 534,14"/>
          <polyline points="2,64 2,76 14,76"/>
          <polyline points="522,76 534,76 534,64"/>
        </g>
      </svg>
      <h1 class="business-name">Marisol Dovey Photography</h1>
    </div>
    <svg class="corner-marks" viewBox="0 0 640 366" aria-hidden="true">
      <g fill="none" stroke="var(--corner-gold)" stroke-width="4">
        <polyline points="4,20 4,4 20,4"/>
        <polyline points="620,4 636,4 636,20"/>
        <polyline points="4,346 4,362 20,362"/>
        <polyline points="620,362 636,362 636,346"/>
      </g>
    </svg>
  </section>

  <section class="card card-back" aria-label="Business card back">
    <div class="owner">
      <svg viewBox="0 0 220 130" preserveAspectRatio="none" aria-hidden="true">
        <g fill="none" stroke="#ffffff" stroke-width="2">
          <polyline points="2,14 2,2 14,2"/>
          <polyline points="206,2 218,2 218,14"/>
          <polyline points="2,116 2,128 14,128"/>
          <polyline points="206,128 218,128 218,116"/>
        </g>
      </svg>
      <h2 class="owner-name">Marisol<br>Pendergast</h2>
    </div>
    <div class="divider"></div>
    <ul class="contact-list">
      <li class="contact-item">
        <svg viewBox="0 0 26 26" aria-hidden="true">
          <circle cx="13" cy="13" r="12" fill="none" stroke="#ffffff" stroke-width="1.5"/>
          <path d="M13 6a4.5 4.5 0 0 1 4.5 4.5c0 3.4-4.5 8.5-4.5 8.5s-4.5-5.1-4.5-8.5A4.5 4.5 0 0 1 13 6z" fill="#ffffff"/>
          <circle cx="13" cy="10.5" r="1.6" fill="var(--card-yellow)"/>
        </svg>
        <span>1295 Wirrabilla-Kontee Road,<br>Kontee Qld 4871</span>
      </li>
      <li class="contact-item contact-phone">
        <svg viewBox="0 0 26 26" aria-hidden="true">
          <circle cx="13" cy="13" r="12" fill="none" stroke="#ffffff" stroke-width="1.5"/>
          <path d="M9.2 7.5l2 0.4 0.9 3-1.3 1.1a7 7 0 0 0 3.2 3.2l1.1-1.3 3 0.9 0.4 2c-0.5 1-1.6 1.7-2.8 1.5-4.2-0.8-7.6-4.2-8.4-8.4-0.2-1.2 0.5-2.3 1.9-2.4z" fill="#ffffff"/>
        </svg>
        <span>0471620394</span>
      </li>
      <li class="contact-item">
        <svg viewBox="0 0 26 26" aria-hidden="true">
          <circle cx="13" cy="13" r="12" fill="none" stroke="#ffffff" stroke-width="1.5"/>
        </svg>
        <span>www.snapfolk.net/MarisolDovey/Photography</span>
      </li>
    </ul>
    <svg class="corner-marks" viewBox="0 0 640 366" aria-hidden="true">
      <g fill="none" stroke="var(--ink)" stroke-width="4">
        <polyline points="4,20 4,4 20,4"/>
        <polyline points="620,4 636,4 636,20"/>
        <polyline points="4,346 4,362 20,362"/>
        <polyline points="620,362 636,362 636,346"/>
      </g>
    </svg>
  </section>

</body>
</html>
```